3 Posters for House Designer

I'm installing a set of 3 posters on our office wall to describe the benefits of our house design services. These posters are A0 size and will be seen from the front windows of the office. I have already purchased the AO snap frames to hold the posters, they are silver in colour.

We, Farlow Studio, design houses. We offer Architectural services but as we didn't study Architecture, we're not permitted to use the word Architect or any derivative there of. So no words allowed that say Architect, Architecture or Architectural and the like.

Each poster will highlight a benefit of engaging Farlow Studio to design a house and the posters will be lined up side by side.

The first benefit is GENUINE PASSION.
I am genuinely passionate about designing homes that fit my clients like a glove in every way. I genuinely care about my clients doing the right thing by themselves and I'm not a "yes man". I challenge myself and my clients to ensure the best possible result.

The second benefit is CREATIVE THINKING.
I love a challenge. I can spend hours, even days, working on one small aspect of a house design to make it work best. I love solving design problems on difficult sites. What I pride myself on is delivering house designs which are as great to live with as they are to look at; form and function, beautiful yet practical.

The third benefit is GUARANTEED RESULTS.
My genuine passion and creative thinking result in my initial house designs being 95% right, for my clients, the first time; requiring very few changes. This is why I offer, iron clad, guarantees which form part of our design contract. These guarantees include:
1. Our clients absolutely loving our design. If they want to change something, we'll change it at no additional cost; no matter how big the changes or how many.
2. We guarantee our house designs will be within the given budget to build the house. If not, we'll amend our design at no additional cost.
3. We guarantee our house designs will meet the required minimum 6 star energy efficiency rating. If not, we'll amend the design at no additional cost.
4. We guarantee Council approval to build as designed. If not, we'll amend our design at no additional cost.

I see each benefit title being the hero on each poster (ie GENUINE PASSION). I see white type on a light blue background. I see A hero shot of stylish houses in the backgrounds but blurred. I see life in the posters in the form of colour and happy people (customers). Our customers are aged between 40 & 60.

I have a logo (uploaded) and have already purchased images of people if required. Please advise if you want these.

Check out our website at www.farlow-studio.com.au/Kelmore

Target Market(s)

Couples aged 40 - 60

Industry/Entity Type

House

Requirements
Must have
• Stylish house images, happy people (couples & families), big, bold, hero titles at the top of each of the three posters.

```html
<!DOCTYPE html>
<html lang="en">
<head>
<meta charset="utf-8">
<title>Farlow Studio – Benefit Posters</title>
<link rel="stylesheet" href="https://fonts.googleapis.com/css2?family=Bebas+Neue&family=Oswald:wght@400;600&display=swap">
<style>
  :root {
    --page: #ffffff;
    --blue-top: #2a80cf;
    --blue-bottom: #1a62ad;
    --band: #3b4047;
    --white: #ffffff;
    --title-shade: #d4d8de;
    --tag-blue: #1b5fa6;
    --shadow: rgba(0, 0, 0, 0.28);
  }
  * { margin: 0; padding: 0; box-sizing: border-box; }
  html, body {
    width: 1200px; height: 592px; overflow: hidden;
    background: var(--page);
  }
  .wall { position: relative; width: 1200px; height: 592px; }

  .poster {
    position: absolute; top: 12px; width: 380px; height: 537px;
    background: linear-gradient(180deg, var(--blue-top) 0%, var(--blue-bottom) 100%);
    overflow: hidden;
  }
  .poster--passion { left: 14px; }
  .poster--creative { left: 410px; }
  .poster--results { left: 810px; }

  .poster-shadow {
    position: absolute; top: 548px; width: 360px; height: 22px;
    border-radius: 50%;
    background: radial-gradient(ellipse at center, var(--shadow) 0%, rgba(0,0,0,0) 70%);
  }

  .poster__photo {
    position: absolute; inset: 0 0 auto 0; height: 240px;
    clip-path: polygon(0 0, 100% 0, 100% 176px, 0 222px);
  }
  .poster--passion .poster__photo {
    background: linear-gradient(160deg, #dfe6e9 0%, #b9b3a2 40%, #5f7d4a 75%, #2c3d66 100%);
  }
  .poster--creative .poster__photo {
    background: linear-gradient(120deg, #b03a34 0%, #c8b9a3 35%, #ece6dc 60%, #b98a5e 100%);
  }
  .poster--results .poster__photo {
    background: linear-gradient(150deg, #e7f0f6 0%, #c7dcea 45%, #5fb3dc 80%, #9bd0ec 100%);
  }

  .poster__band {
    position: absolute; inset: 0 0 auto 0; height: 250px;
    background: var(--band);
    clip-path: polygon(0 222px, 100% 176px, 100% 190px, 0 238px);
  }

  .poster__title {
    position: absolute; top: 248px; left: 0; right: 0;
    text-align: center;
    font-family: "Bebas Neue", "Oswald", sans-serif;
    font-size: 72px; line-height: 60px; letter-spacing: 1px;
    color: var(--white);
    background: linear-gradient(180deg, var(--white) 45%, var(--title-shade) 100%);
    -webkit-background-clip: text; background-clip: text;
    -webkit-text-fill-color: transparent;
    filter: drop-shadow(0 3px 3px rgba(0,0,0,0.35));
  }

  .poster__tagline {
    position: absolute; top: 398px; left: 0; right: 0;
    text-align: center;
  }
  .poster__tagline span {
    display: inline-block; background: var(--white);
    color: var(--tag-blue);
    font-family: "Oswald", sans-serif; font-weight: 600;
    font-size: 16px; line-height: 24px; padding: 0 6px;
    text-transform: uppercase;
  }

  .poster__brand {
    position: absolute; top: 466px; left: 0; right: 0;
    text-align: center; color: var(--white);
  }
  .poster__brand-name {
    font-family: "Oswald", sans-serif; font-weight: 400;
    font-size: 28px; line-height: 34px; color: var(--white);
  }
  .poster__brand-line {
    font-family: "Oswald", sans-serif; font-weight: 400;
    font-size: 6.5px; letter-spacing: 0.4px; color: var(--white);
  }
</style>
</head>
<body>
<main class="wall">

  <section class="poster poster--passion">
    <div class="poster__photo" role="img" aria-label="Couple standing arm in arm in front of their new two-storey home"></div>
    <div class="poster__band"></div>
    <h2 class="poster__title">Genuine<br>Passion</h2>
    <p class="poster__tagline"><span>To fulfill your dreams</span></p>
    <div class="poster__brand">
      <div class="poster__brand-name">Farlow Studio</div>
      <div class="poster__brand-line">RESIDENTIAL DESIGNERS PERTH, WESTERN AUSTRALIA</div>
    </div>
  </section>
  <div class="poster-shadow" style="left:24px"></div>

  <section class="poster poster--creative">
    <div class="poster__photo" role="img" aria-label="Bright modern living room with a red feature wall and timber panelling"></div>
    <div class="poster__band"></div>
    <h2 class="poster__title">Creative<br>Thinking</h2>
    <p class="poster__tagline"><span>We love solving problems</span></p>
    <div class="poster__brand">
      <div class="poster__brand-name">Farlow Studio</div>
      <div class="poster__brand-line">RESIDENTIAL DESIGNERS PERTH, WESTERN AUSTRALIA</div>
    </div>
  </section>
  <div class="poster-shadow" style="left:420px"></div>

  <section class="poster poster--results">
    <div class="poster__photo" role="img" aria-label="Two laughing children lying on cushions at home"></div>
    <div class="poster__band"></div>
    <h2 class="poster__title">Guaranteed<br>Results</h2>
    <p class="poster__tagline"><span>Designed with you in mind</span></p>
    <div class="poster__brand">
      <div class="poster__brand-name">Farlow Studio</div>
      <div class="poster__brand-line">RESIDENTIAL DESIGNERS PERTH, WESTERN AUSTRALIA</div>
    </div>
  </section>
  <div class="poster-shadow" style="left:820px"></div>

</main>
</body>
</html>
```